Blog based website for baseball.

I am a college baseball coach looking to create a blog type site that uses content to keep readers coming back and eventually trusting me enough to buy my products.

I am an author, coach, writer, speaker with a bunch sites now, but I want to make one main site that people can come back to and see new content over and over..

Target Market(s)

High school baseball players and parents.

Industry/Entity Type

Education

Number of Pages Required

4 page

Font styles to use
Sans Serif

Requirements
Must have
• 1) An about page. 2) Either commerce page or link to my other commerce pages. 3) Featured blog but also access to past blogs. 4) Featured product of the week (maybe in side bar). 5) Places to opt in and join the list. 6) A way to share the content people like.
Nice to have
• No idea the difference between uncoded and coded!
• I like the idea of an opt in pop up.

```html
<!DOCTYPE html>
<html lang="en">
<head>
<meta charset="utf-8">
<title>Diamond Prep — Blog</title>
<link href="https://fonts.googleapis.com/css2?family=Roboto:wght@300;400;500;700&display=swap" rel="stylesheet">
<style>
:root{
  --red:#e3161b;
  --blue:#2347b8;
  --btn-blue:#1536cc;
  --ink:#222;
  --muted:#666;
  --rule:#cfcfcf;
  --panel:#ececec;
  --dark:#2a2a2a;
  --footer:#424242;
}
*{box-sizing:border-box;margin:0;padding:0}
html,body{width:780px;height:1200px;overflow:hidden;background:#fff}
body{font-family:"Roboto",Arial,sans-serif;color:var(--ink);position:relative}
.site-header{position:absolute;left:0;top:0;width:780px;height:59px;background:#fff;box-shadow:0 1px 3px rgba(0,0,0,.12);z-index:2}
.brand{position:absolute;left:50px;top:19px;display:flex;align-items:center;gap:6px;font-size:17px;font-weight:700;color:var(--blue);letter-spacing:-.3px}
.brand-dot{width:18px;height:18px;border-radius:50%;background:var(--red)}
.main-nav{position:absolute;top:31px;left:0;font-size:8.5px}
.main-nav a{position:absolute;white-space:nowrap;color:var(--ink);text-decoration:none}
.main-nav a.active{color:var(--blue);font-weight:500}
.search{position:absolute;left:615px;top:27px;width:116px;height:19px;border:1px solid #ccc;background:#f7f7f7;font-size:7.5px;color:#999;font-style:italic;padding:5px 7px}
.search svg{position:absolute;right:5px;top:4px}
.hero{position:absolute;left:0;top:59px;width:780px;height:279px;background:linear-gradient(180deg,#b9c6c3 0%,#c9a9ab 30%,#b73b43 58%,#d8d4d2 78%,#6d5a55 100%)}
.hero-dots{position:absolute;left:363px;top:313px;display:flex;gap:4px}
.hero-dots span{width:10px;height:10px;border-radius:50%;background:#111}
.hero-dots span.on{background:#1c4fd8}
.content{position:absolute;left:49px;top:360px;width:508px}
.section-title{font-size:18px;font-weight:400;color:var(--red);height:33px;border-bottom:1px solid var(--rule)}
.post{position:relative;height:227px;border-bottom:1px solid var(--rule)}
.post-title{position:absolute;left:0;top:14px;width:320px;font-size:14.4px;font-weight:300;line-height:18px;color:var(--blue)}
.post-meta{position:absolute;left:0;top:54px;font-size:8px;color:#333}
.post-meta a{color:var(--red);text-decoration:none}
.post-actions{position:absolute;right:0;top:33px;display:flex;align-items:center;font-size:7.5px}
.likes{display:flex;align-items:center;gap:5px;color:var(--red);margin-right:18px}
.share{display:flex;align-items:center;gap:6px;color:#333}
.post-divider{position:absolute;left:0;right:0;top:76px;border-top:1px dashed #bbb}
.post-image{position:absolute;left:0;top:91px;width:209px;height:111px;border:1px solid #ccc}
.post-excerpt{position:absolute;left:224px;top:90px;width:284px;font-size:8px;line-height:14.4px;color:#555}
.btn{display:inline-block;text-align:center;color:#fff;text-decoration:none}
.read-more{position:absolute;left:224px;top:183px;width:68px;height:20px;line-height:20px;font-size:8px;background:var(--btn-blue)}
.pagination{position:absolute;left:0;width:508px;top:742px;display:flex;justify-content:center;gap:6px;font-size:9px}
.pagination span{width:17px;height:17px;line-height:17px;text-align:center}
.pagination .arrow{background:#ddd;color:#444;margin:0 6px}
.pagination .current{background:var(--red);color:#fff}
.sidebar{position:absolute;left:574px;top:365px;width:157px}
.featured{background:var(--panel);height:327px;text-align:center}
.featured-head{background:var(--dark);color:#fff;height:65px;font-size:16px;font-weight:300;line-height:20px;padding-top:13px}
.product-cover{display:block;margin:22px auto 0;width:96px;height:128px;background:linear-gradient(135deg,#e9e9ea,#b9c3d4 55%,#3b4a7a)}
.product-name{font-size:17px;font-weight:300;color:var(--blue);margin-top:10px}
.product-desc{font-size:8px;line-height:14px;color:#555;margin-top:4px;padding:0 14px}
.product-btn{width:76px;height:24px;line-height:24px;background:var(--red);font-size:9px;font-weight:500;letter-spacing:.3px;margin-top:10px}
.widget{background:var(--panel);margin-top:10px;padding:12px 12px 0}
.widget h3{font-size:17px;font-weight:300;color:#222}
.join{height:116px}
.email{margin-top:10px;height:25px;background:#fff;font-size:7.5px;color:#666;padding:8px 9px}
.join-btn{display:block;margin:9px 0 0 auto;width:67px;height:19px;line-height:19px;background:var(--btn-blue);font-size:8px}
.connect{height:80px}
.social{display:flex;gap:4px;margin-top:7px}
.social span{width:29px;height:29px;border-radius:50%;border:1.5px solid}
.site-footer{position:absolute;left:0;top:1131px;width:780px;height:69px;background:var(--footer);text-align:center;font-size:8px;line-height:13px;color:#aaa;padding-top:27px}
</style>
</head>
<body>
<header class="site-header">
  <div class="brand"><span class="brand-dot"></span>Diamond Prep</div>
  <nav class="main-nav">
    <a class="active" style="left:270px" href="#">Home</a>
    <a style="left:325px" href="#">Blog Post</a>
    <a style="left:394px" href="#">Product of the Week</a>
    <a style="left:504px" href="#">Join List</a>
    <a style="left:562px" href="#">Contact</a>
  </nav>
  <div class="search">Search...
    <svg width="10" height="10" viewBox="0 0 10 10"><circle cx="6" cy="4" r="3" fill="none" stroke="#333" stroke-width="1.3"/><path d="M4 6 L1 9" stroke="#333" stroke-width="1.6"/></svg>
  </div>
</header>

<section class="hero" role="img" aria-label="Team photo of a college baseball squad in red jerseys posing on the field">
</section>
<div class="hero-dots"><span class="on"></span><span></span><span></span><span></span></div>

<main class="content">
  <h2 class="section-title">Latest Post</h2>

  <article class="post">
    <h3 class="post-title">Vestibulum vel metus sit amet turpis bibendum tincidunt vel sit amet quam...</h3>
    <p class="post-meta">Posted on 3 days ago &nbsp;|&nbsp; By <a href="#">Coach Dell</a></p>
    <div class="post-actions">
      <span class="likes"><svg width="15" height="13" viewBox="0 0 16 14"><path d="M8 14 L1.5 7.5 A4 4 0 0 1 8 2.5 A4 4 0 0 1 14.5 7.5 Z" fill="#666"/></svg>250 Likes</span>
      <span class="share"><svg width="15" height="10" viewBox="0 0 15 10"><path d="M0 2 H4 L9 8 H13 M0 8 H4 L9 2 H13" fill="none" stroke="#444" stroke-width="1.3"/><path d="M11 0 L14 2 L11 4 M11 6 L14 8 L11 10" fill="none" stroke="#444" stroke-width="1.2"/></svg>Share</span>
    </div>
    <div class="post-divider"></div>
    <div class="post-image" role="img" aria-label="Coach portrait beside a baseball recruiting banner over a stadium" style="background:linear-gradient(90deg,#c9a89a 0%,#d9d9de 30%,#5a79a8 60%,#c8362f 85%,#e4e4e4 100%)"></div>
    <p class="post-excerpt">Aliquam molestie, mi et imperdiet euismod, dui purus auctor tellus, et interdum lacus lectus et ante. Sed accumsan sollicitudin sapien, sit amet adipiscing turpis gravida ac. In congue, neque ac lobortis volutpat, libero mauris varius mi, vitae suscipit ipsum ligula vitae risus. Duis aliquam nibh a dui iaculis viverra id a velit. Vivamus egestas risus in magna varius commodo. Sed semper viverra egestas.</p>
    <a class="btn read-more" href="#">READ MORE</a>
  </article>

  <article class="post">
    <h3 class="post-title">Vestibulum vel metus sit amet turpis bibendum tincidunt vel sit amet quam...</h3>
    <p class="post-meta">Posted on 3 days ago &nbsp;|&nbsp; By <a href="#">Coach Dell</a></p>
    <div class="post-actions">
      <span class="likes"><svg width="15" height="13" viewBox="0 0 16 14"><path d="M8 14 L1.5 7.5 A4 4 0 0 1 8 2.5 A4 4 0 0 1 14.5 7.5 Z" fill="#666"/></svg>250 Likes</span>
      <span class="share"><svg width="15" height="10" viewBox="0 0 15 10"><path d="M0 2 H4 L9 8 H13 M0 8 H4 L9 2 H13" fill="none" stroke="#444" stroke-width="1.3"/><path d="M11 0 L14 2 L11 4 M11 6 L14 8 L11 10" fill="none" stroke="#444" stroke-width="1.2"/></svg>Share</span>
    </div>
    <div class="post-divider"></div>
    <div class="post-image" role="img" aria-label="Ballpark infield seen from the stands" style="background:linear-gradient(180deg,#9fb3c9 0%,#7e6f62 28%,#4f7b3c 45%,#b98b63 62%,#3f6b33 80%,#2c3a4a 100%)"></div>
    <p class="post-excerpt">Aliquam molestie, mi et imperdiet euismod, dui purus auctor tellus, et interdum lacus lectus et ante. Sed accumsan sollicitudin sapien, sit amet adipiscing turpis gravida ac. In congue, neque ac lobortis volutpat, libero mauris varius mi, vitae suscipit ipsum ligula vitae risus. Duis aliquam nibh a dui iaculis viverra id a velit. Vivamus egestas risus in magna varius commodo.</p>
    <a class="btn read-more" href="#">READ MORE</a>
  </article>

  <article class="post">
    <h3 class="post-title">Vestibulum vel metus sit amet turpis bibendum tincidunt vel sit amet quam...</h3>
    <p class="post-meta">Posted on 3 days ago &nbsp;|&nbsp; By <a href="#">Coach Dell</a></p>
    <div class="post-actions">
      <span class="likes"><svg width="15" height="13" viewBox="0 0 16 14"><path d="M8 14 L1.5 7.5 A4 4 0 0 1 8 2.5 A4 4 0 0 1 14.5 7.5 Z" fill="#666"/></svg>250 Likes</span>
      <span class="share"><svg width="15" height="10" viewBox="0 0 15 10"><path d="M0 2 H4 L9 8 H13 M0 8 H4 L9 2 H13" fill="none" stroke="#444" stroke-width="1.3"/><path d="M11 0 L14 2 L11 4 M11 6 L14 8 L11 10" fill="none" stroke="#444" stroke-width="1.2"/></svg>Share</span>
    </div>
    <div class="post-divider"></div>
    <div class="post-image" role="img" aria-label="Four players in red shirts holding award certificates on the field" style="background:linear-gradient(180deg,#c7d2dc 0%,#a7b39b 35%,#c23a34 60%,#8e2a2a 80%,#5c6b45 100%)"></div>
    <p class="post-excerpt">Aliquam molestie, mi et imperdiet euismod, dui purus auctor tellus, et interdum lacus lectus et ante. Sed accumsan sollicitudin sapien, sit amet adipiscing turpis gravida ac. In congue, neque ac lobortis volutpat, libero mauris varius mi, vitae suscipit ipsum ligula vitae risus. Duis aliquam nibh a dui iaculis viverra id a velit. Vivamus egestas risus in magna varius commodo. Sed semper viverra egestas.</p>
    <a class="btn read-more" href="#">READ MORE</a>
  </article>

  <nav class="pagination">
    <span class="arrow">‹‹</span><span class="current">1</span><span>2</span><span>3</span><span>4</span><span>5</span><span class="arrow">››</span>
  </nav>
</main>

<aside class="sidebar">
  <section class="featured">
    <h3 class="featured-head">Featured Product<br>of the Week</h3>
    <div class="product-cover" role="img" aria-label="Book cover: a guide to college baseball for high school athletes"></div>
    <h4 class="product-name">College Baseball</h4>
    <p class="product-desc">Vivamus egestas risus in magna varius commodo.</p>
    <a class="btn product-btn" href="#">READ MORE</a>
  </section>

  <section class="widget join">
    <h3>Join Listing</h3>
    <div class="email">Enter Email</div>
    <a class="btn join-btn" href="#">JOIN NOW</a>
  </section>

  <section class="widget connect">
    <h3>Connect</h3>
    <div class="social">
      <span style="border-color:#3b5998" aria-label="Social profile 1"></span>
      <span style="border-color:#2aa3d8" aria-label="Social profile 2"></span>
      <span style="border-color:#1f75a8" aria-label="Social profile 3"></span>
      <span style="border-color:#e8741f" aria-label="News feed"></span>
    </div>
  </section>
</aside>

<footer class="site-footer">
  Copyright © 2015.Company Name. All Right Reserved<br>Privacy Policy
</footer>
</body>
</html>
```